Fall Festival & Movie Night

This is small church that is reaching out to the community to spread the gospel. We are having a free food, drinks, games and a free movie. I want the post card to read:
Free Food & Drinks
Free Games
Free Movie - Rivers Still Run
When: Saturday, October 11th
Games and Food start at 4:00 pm
Movie starts at 6:15 pm
Where: 4619 Marlow Lane South Chesterfield - Future Home of Brookhaven Fellowship Church
Rain Date: October 18th
Updates
To all designers:
Thank you so much for your hard work and creative postcards. We have decided to go with design #4544179 from designer "tarnwick". This designer has illustrated and captured the feel of our event from the very beginning and we are very pleased to go with that design. It still has a couple last minute details so this project remains open; however, as a courtesy do not submit any more designs as to not "waste" your very valuable time.
Once again many thanks. :)
Industry/Entity Type
Church
Font styles to use
Requirements
Must have
- Have oversized post cards in possession by October 3rd. Please send in designs as soon as possible.
Nice to have
- Country Background (open grassy area, with trees outlining property. location is Chesterfield, Virginia). three wooden crosses would be nice. also people talking and eating on grassy area would work.

```html
<!DOCTYPE html>
<html lang="en">
<head>
<meta charset="utf-8">
<title>Brookhaven Fellowship Church – Outreach Card</title>
<link href="https://fonts.googleapis.com/css2?family=Montserrat:wght@900&family=Archivo+Narrow:ital,wght@0,400;0,500;1,400;1,500&family=Roboto:wght@300;400;500&display=swap" rel="stylesheet">
<style>
  :root {
    --magenta: #e22bd8;
    --magenta-bright: #ff4ff2;
    --paper: #ffffff;
    --panel: #1f2225;
    --panel-text: #e2e2e2;
    --sky-top: #b7c8dc;
    --sky-mid: #8e9cb4;
    --city: #5a5f74;
    --glow: #8a6a52;
    --grass: #3f4c32;
    --crowd: #25282d;
  }
  * { margin: 0; padding: 0; box-sizing: border-box; }
  html, body { width: 1200px; height: 1000px; overflow: hidden; background: var(--paper); }
  .sheet { position: relative; width: 1200px; height: 1000px; }

  .cards { position: absolute; left: 0; top: 0; width: 622px; height: 1000px; background: var(--paper); }
  .card { position: absolute; left: 0; width: 622px; overflow: hidden; }
  .card--front { top: 15px; height: 452px; }
  .card--back { top: 518px; height: 482px; }
  .divider-band { position: absolute; left: 0; top: 478px; width: 622px; height: 27px; background: var(--magenta); }

  .scene-photo {
    position: absolute; inset: 0;
    background: linear-gradient(180deg,
      var(--sky-top) 0%,
      var(--sky-mid) 16%,
      var(--city) 34%,
      var(--glow) 44%,
      var(--grass) 54%,
      #343b2c 72%,
      var(--crowd) 100%);
  }

  .headline {
    position: absolute; left: 18px;
    font-family: "Montserrat", sans-serif; font-weight: 900;
    color: var(--magenta); font-size: 60px; line-height: 67px;
    letter-spacing: 0.5px; text-transform: uppercase;
    text-shadow: 0 2px 6px rgba(0, 0, 0, 0.25);
  }
  .headline--top { top: 38px; }
  .headline--bottom { top: 250px; }

  .card-brand {
    position: absolute; left: 16px; top: 428px;
    font-family: "Roboto", sans-serif; font-weight: 400; font-size: 16px;
    color: #fff; text-transform: uppercase;
  }
  .card-brand strong { font-weight: 500; }

  .spotlight {
    position: absolute; left: 140px; top: 57px; width: 340px; height: 340px;
    border-radius: 50%;
    background: rgba(18, 26, 40, 0.62);
    box-shadow: 0 0 0 1px rgba(180, 220, 240, 0.25);
  }
  .details {
    position: absolute; left: 0; width: 622px; top: 150px;
    font-family: "Archivo Narrow", sans-serif; font-weight: 500; font-size: 20px; line-height: 28px;
    color: var(--magenta-bright); text-align: center; text-transform: uppercase; list-style: none;
  }
  .details .timing { font-style: italic; }
  .event-when {
    position: absolute; left: 18px; top: 388px;
    font-family: "Archivo Narrow", sans-serif; font-weight: 500; font-size: 17px; line-height: 25px;
    color: var(--magenta-bright); text-transform: uppercase;
    text-shadow: 0 1px 3px rgba(0, 0, 0, 0.6);
  }
  .event-when .rain { text-transform: none; }

  .rule { position: absolute; left: 622px; top: 0; width: 4px; height: 1000px; background: var(--magenta); }

  .panel {
    position: absolute; left: 626px; top: 0; width: 574px; height: 1000px;
    background: linear-gradient(160deg, #24262a 0%, var(--panel) 60%, #1b1d20 100%);
  }
  .panel-title {
    position: absolute; left: 26px; top: 66px;
    font-family: "Roboto", sans-serif; color: var(--panel-text);
    font-size: 44px; line-height: 56px; text-transform: uppercase;
  }
  .panel-title .first { font-weight: 400; display: block; }
  .panel-title .rest { font-weight: 300; display: block; }
  .panel-sub {
    position: absolute; left: 30px; top: 179px;
    font-family: "Roboto", sans-serif; font-size: 20px; font-weight: 400;
    color: var(--magenta); text-transform: uppercase;
  }
</style>
</head>
<body>
<main class="sheet">
  <section class="cards">
    <article class="card card--front">
      <div class="scene-photo" role="img" aria-label="Photo of a crowd on a grassy park lawn at dusk watching an outdoor movie screen, city towers behind"></div>
      <h1 class="headline headline--top">You’re invited!</h1>
      <h2 class="headline headline--bottom">To a night<br>of community!</h2>
      <p class="card-brand"><strong>Brookhaven</strong> Fellowship Church</p>
    </article>

    <div class="divider-band"></div>

    <article class="card card--back">
      <div class="scene-photo" role="img" aria-label="Photo of a crowd on a grassy park lawn at dusk awaiting an outdoor movie, city towers behind"></div>
      <div class="spotlight"></div>
      <ul class="details">
        <li>Free food &amp; drinks</li>
        <li>Free games</li>
        <li>Premiere of <em>Rivers Still Run</em></li>
        <li class="timing">Food &amp; games begin at 4:00pm</li>
        <li class="timing">Movie will begin at 6:15pm</li>
      </ul>
      <p class="event-when">
        Saturday October, 11th @<br>
        4619 Marlow Lane South Chesterfield<br>
        <span class="rain">(Rain Date October 18th)</span>
      </p>
    </article>
  </section>

  <div class="rule"></div>

  <aside class="panel">
    <h2 class="panel-title"><span class="first">Brookhaven</span><span class="rest">Fellowship Church</span></h2>
    <p class="panel-sub">Outreach card</p>
  </aside>
</main>
</body>
</html>
```